In Home Personal IT Consultant (Nerd) Website and Logo LOpalo.com

Website and logo design for in home personal "nerd". Consulting services provided: Home Automation, Home Theater, Network and Wi-Fi installation, Computer Repair, and Virus Removal. Need simple site to promote LOpalo.com based in Santa Fe, New Mexico. You may choose to incorporate the Zia symbol from the New Mexico flag into the design, not mandatory. I am also a big fan of the movie Summer at Crane Lake.
I have over 10 years of experience in the hospitality industry working with multi million dollar hotels and will apply that same level of service to the home. Veltrona K7 and Bulwark+ Certified. Available by appointment, primarily Evenings and Weekends. Consulting rate will be $70/hr.
Consulting
1 page

```html
<!DOCTYPE html>
<html lang="en">
<head>
<meta charset="utf-8">
<title>LOpalo – In Home Personal IT Consultant</title>
<link rel="stylesheet" href="https://fonts.googleapis.com/css2?family=Open+Sans:wght@400;600;700;800&family=Montserrat:wght@400;500;600&family=Roboto:wght@400;500&display=swap">
<style>
:root{
  --red:#c8102e;
  --blue:#0a6cbc;
  --charcoal:#414141;
  --footer:#444444;
  --ink:#111111;
  --muted:#555555;
  --line:#d8d8d8;
  --grey-band:#ececee;
  --white:#ffffff;
}
*{margin:0;padding:0;box-sizing:border-box}
html,body{width:1200px;height:2671px;overflow:hidden;background:var(--white)}
body{position:relative;font-family:"Roboto",Arial,sans-serif;color:var(--ink)}
.abs{position:absolute}

/* header */
.brand{left:133px;top:30px;display:flex;align-items:center;gap:12px}
.brand-mark{width:40px;height:40px;background:var(--red)}
.brand-name{font:800 22px "Open Sans",sans-serif;color:var(--ink);letter-spacing:.5px}
.call{left:797px;top:18px;display:flex;align-items:center;gap:12px}
.call-icon{width:32px;height:32px;border-radius:50%;background:var(--red);display:flex;align-items:center;justify-content:center}
.call-label{font:600 10px "Open Sans",sans-serif;color:#333;letter-spacing:.3px}
.call-number{font:700 20px "Open Sans",sans-serif;color:var(--red);line-height:1}
.search{left:975px;top:22px;width:93px;height:26px;border:1px solid #ccc;font:9px "Open Sans",sans-serif;color:#777;padding:7px 8px}
.search svg{position:absolute;right:6px;top:8px}
.nav{left:576px;top:68px;display:flex;gap:0;font:700 10.5px "Open Sans",sans-serif;letter-spacing:.3px}
.nav a{color:#222;text-decoration:none;padding:5px 12px;margin-right:14px}
.nav a.active{color:var(--red);border:1.5px solid var(--red)}

/* hero */
.hero{left:0;top:100px;width:1200px;height:583px;background:radial-gradient(ellipse at 55% 55%,#8b6a55 0%,#5a3a2c 45%,#2e1c16 100%)}
.hero-title{left:0;top:146px;width:1200px;text-align:center;font:800 35px "Open Sans",sans-serif;color:var(--white);letter-spacing:.5px}
.hero-sub{left:0;top:186px;width:1200px;text-align:center;font:400 18px "Open Sans",sans-serif;color:#eee}
.btn{display:inline-block;background:var(--red);color:var(--white);font:600 11px "Montserrat",sans-serif;letter-spacing:.4px;text-align:center}
.hero-btn{left:532px;top:231px;width:136px;height:40px;line-height:40px;font:700 14px "Open Sans",sans-serif;border:2px solid #fff}
.arrow{width:50px;height:50px;border-radius:50%;border:2px solid #fff;display:flex;align-items:center;justify-content:center}
.arrow-left{left:107px;top:365px}
.arrow-right{left:1045px;top:365px;background:rgba(255,255,255,.9);border-color:var(--red)}

/* section titles */
.section-title{left:0;width:1200px;text-align:center;font:700 19px "Open Sans",sans-serif;color:var(--ink)}
.divider{left:583px;width:36px;height:10px}

/* services */
.grid-line{background:var(--line)}
.service{width:300px;text-align:center}
.service-name{font:500 12.5px "Montserrat",sans-serif;color:#111;margin:14px 0 16px}
.service-text{font:400 10.5px/1.5 "Roboto",sans-serif;color:#444;width:200px;margin:0 auto}
.view-all{left:531px;top:1087px;width:136px;height:28px;line-height:28px;font-size:10.5px}

.band{top:1262px;height:62px;line-height:62px;color:#fff;font:500 12.5px "Montserrat",sans-serif;text-align:center;letter-spacing:.3px}
.band-blue{left:133px;width:296px;background:var(--blue)}
.band-dark{left:450px;width:298px;background:var(--charcoal)}
.band-red{left:769px;width:296px;background:var(--red)}

/* welcome */
.welcome{left:0;top:1385px;width:1200px;height:431px;background:var(--grey-band)}
.welcome-text{left:370px;top:1536px;width:460px;text-align:center;font:400 11.5px/1.55 "Roboto",sans-serif;color:#333}
.cert{height:62px;background:var(--white);border:3px solid var(--red)}
.read-more-center{left:550px;top:1800px;width:111px;height:27px;line-height:27px;font-size:10px}

/* blog */
.card{top:1987px;width:298px;height:366px;border:1px solid #e2e2e2;background:#fff}
.card-photo{position:absolute;left:11px;top:16px;width:275px;height:180px}
.card-title{position:absolute;left:23px;top:212px;width:255px;font:400 13.5px/1.4 "Roboto",sans-serif;color:#111}
.card-text{position:absolute;left:23px;top:257px;width:255px;font:400 10.5px/1.5 "Roboto",sans-serif;color:#666;text-align:justify}
.card-btn{position:absolute;left:23px;top:322px;width:80px;height:21px;line-height:21px;font-size:9px}

/* footer */
.footer{left:0;top:2410px;width:1200px;height:261px;background:var(--footer);color:#eee}
.footer-brand{left:145px;top:2500px;display:flex;align-items:center;gap:12px}
.footer-brand .brand-mark{width:44px;height:44px}
.footer-brand .brand-name{color:#fff;font-size:21px}
.copyright{left:145px;top:2576px;font:400 9.5px "Roboto",sans-serif;color:#eee}
.foot-head{top:2455px;font:700 11px "Montserrat",sans-serif;color:#fff;letter-spacing:.3px}
.foot-item{font:400 10px/1.5 "Roboto",sans-serif;color:#ddd;display:flex;gap:14px;align-items:flex-start}
.menu-list{left:688px;top:2490px;list-style:none;font:400 10px/1.6 "Roboto",sans-serif;color:#eee}
.social{left:884px;top:2490px;display:flex;gap:7px}
.social span{width:27px;height:27px;border-radius:50%;background:var(--blue)}
</style>
</head>
<body>

<!-- header -->
<div class="abs brand"><span class="brand-mark"></span><span class="brand-name">LOpalo</span></div>
<div class="abs call">
  <span class="call-icon"><svg width="14" height="14" viewBox="0 0 24 24"><path fill="#fff" d="M6.6 10.8c1.4 2.8 3.8 5.1 6.6 6.6l2.2-2.2c.3-.3.7-.4 1-.2 1.1.4 2.3.6 3.6.6.6 0 1 .4 1 1V20c0 .6-.4 1-1 1C10.6 21 3 13.4 3 4c0-.6.4-1 1-1h3.5c.6 0 1 .4 1 1 0 1.3.2 2.5.6 3.6.1.3 0 .7-.2 1L6.6 10.8z"/></svg></span>
  <div><div class="call-label">CALL US NOW</div><div class="call-number">888.888.8888</div></div>
</div>
<div class="abs search">SEARCH<svg width="9" height="9" viewBox="0 0 10 10"><circle cx="4" cy="4" r="3" fill="none" stroke="#333" stroke-width="1.4"/><line x1="6.2" y1="6.2" x2="9" y2="9" stroke="#333" stroke-width="1.4"/></svg></div>
<nav class="abs nav"><a class="active">HOME</a><a>ABOUT US</a><a>SERVICES</a><a>BLOG</a><a>TESTIMONIALS</a><a>CONTACT US</a></nav>

<!-- hero -->
<div class="abs hero" role="img" aria-label="Hand tapping a home control tablet in a warmly lit living room"></div>
<div class="abs hero-title">HOME AUTOMATION</div>
<div class="abs hero-sub">Lorem Ipsum is simply dummy</div>
<div class="abs btn hero-btn">READ MORE</div>
<div class="abs arrow arrow-left"><svg width="14" height="14" viewBox="0 0 14 14"><path d="M9 2 4 7l5 5" fill="none" stroke="#fff" stroke-width="2"/></svg></div>
<div class="abs arrow arrow-right"><svg width="14" height="14" viewBox="0 0 14 14"><path d="M5 2l5 5-5 5" fill="none" stroke="#c8102e" stroke-width="2"/></svg></div>

<!-- services -->
<div class="abs section-title" style="top:728px">OUR SERVICES</div>
<svg class="abs divider" style="top:774px" viewBox="0 0 36 10"><line x1="0" y1="5" x2="36" y2="5" stroke="#c8102e" stroke-width="2"/><ellipse cx="18" cy="5" rx="7" ry="4.5" fill="#fff" stroke="#c8102e" stroke-width="2"/></svg>

<div class="abs grid-line" style="left:435px;top:810px;width:1px;height:404px"></div>
<div class="abs grid-line" style="left:765px;top:810px;width:1px;height:404px"></div>
<div class="abs grid-line" style="left:133px;top:1003px;width:302px;height:1px"></div>
<div class="abs grid-line" style="left:766px;top:1003px;width:302px;height:1px"></div>

<div class="abs service" style="left:117px;top:803px">
  <svg width="36" height="42" viewBox="0 0 36 42"><rect x="8" y="2" width="8" height="38" rx="2" fill="#c8102e"/><rect x="20" y="2" width="8" height="38" rx="2" fill="#c8102e"/><circle cx="12" cy="12" r="2" fill="#fff"/><circle cx="12" cy="26" r="2.5" fill="#fff"/><circle cx="24" cy="12" r="2" fill="#fff"/><circle cx="24" cy="26" r="2.5" fill="#fff"/><path d="M4 14q-3 7 0 14M32 14q3 7 0 14" fill="none" stroke="#c8102e" stroke-width="1.5"/></svg>
  <div class="service-name">Home Theater</div>
  <div class="service-text">Lorem Ipsum has been the industry's standard dummy text ever since the 1500s, when an unknown.</div>
</div>

<div class="abs service" style="left:785px;top:803px">
  <svg width="44" height="38" viewBox="0 0 44 38"><rect x="3" y="2" width="38" height="26" rx="2" fill="#c8102e"/><rect x="7" y="6" width="30" height="18" fill="#fff"/><circle cx="22" cy="15" r="5" fill="#c8102e"/><circle cx="22" cy="15" r="2" fill="#fff"/><rect x="17" y="28" width="10" height="5" fill="#c8102e"/><rect x="11" y="33" width="22" height="3" fill="#c8102e"/></svg>
  <div class="service-name">Computer Repair</div>
  <div class="service-text">Lorem Ipsum has been the industry's standard dummy text ever since the 1500s, when an unknown.</div>
</div>

<div class="abs service" style="left:450px;top:904px">
  <svg width="50" height="50" viewBox="0 0 50 50"><path d="M8 25a17 17 0 0 1 30-11M42 25a17 17 0 0 1-30 11" fill="none" stroke="#c8102e" stroke-width="2"/><path d="M38 8v7h-7M12 42v-7h7" fill="none" stroke="#c8102e" stroke-width="2"/><path d="M16 25l9-8 9 8v9H16z" fill="none" stroke="#c8102e" stroke-width="2"/><rect x="22" y="26" width="3" height="3" fill="#c8102e"/><rect x="26" y="26" width="3" height="3" fill="#c8102e"/><rect x="22" y="30" width="3" height="3" fill="#c8102e"/><rect x="26" y="30" width="3" height="3" fill="#c8102e"/></svg>
  <div class="service-name" style="margin-top:22px">Home Automation</div>
  <div class="service-text">There are many variations of passages of Lorem Ipsum available.</div>
</div>
<div class="abs btn view-all">VIEW ALL SERVICES</div>

<div class="abs service" style="left:117px;top:1046px">
  <svg width="48" height="36" viewBox="0 0 48 36"><path d="M3 12a30 30 0 0 1 42 0" fill="none" stroke="#c8102e" stroke-width="5" stroke-linecap="round"/><path d="M11 20a19 19 0 0 1 26 0" fill="none" stroke="#c8102e" stroke-width="5" stroke-linecap="round"/><path d="M18 27a9 9 0 0 1 12 0" fill="none" stroke="#c8102e" stroke-width="5" stroke-linecap="round"/><circle cx="24" cy="33" r="3" fill="#c8102e"/></svg>
  <div class="service-name">Network and Wi-Fi installation</div>
  <div class="service-text">Lorem Ipsum has been the industry's standard dummy text ever since the 1500s, when an unknown.</div>
</div>

<div class="abs service" style="left:785px;top:1036px">
  <svg width="48" height="48" viewBox="0 0 48 48"><rect x="3" y="4" width="42" height="36" rx="2" fill="none" stroke="#c8102e" stroke-width="2"/><line x1="3" y1="12" x2="45" y2="12" stroke="#c8102e" stroke-width="2"/><circle cx="8" cy="8" r="1.3" fill="#c8102e"/><circle cx="12" cy="8" r="1.3" fill="#c8102e"/><circle cx="16" cy="8" r="1.3" fill="#c8102e"/><ellipse cx="30" cy="30" rx="6" ry="7" fill="none" stroke="#c8102e" stroke-width="2"/><path d="M22 24l4 3M38 24l-4 3M21 31h3M36 31h3M23 38l3-3M37 38l-3-3M26 20l2 3M34 20l-2 3" stroke="#c8102e" stroke-width="2"/></svg>
  <div class="service-name" style="margin-top:10px">Virus Removal</div>
  <div class="service-text">Lorem Ipsum has been the industry's standard dummy text ever since the 1500s, when an unknown.</div>
</div>

<div class="abs band band-blue">AVAILABLE BY APPOINTMENT</div>
<div class="abs band band-dark">PRIMARILY EVENINGS AND WEEKENDS</div>
<div class="abs band band-red">CONSULTING RATE WILL BE $70/HR</div>

<!-- welcome -->
<div class="abs welcome"></div>
<div class="abs section-title" style="top:1436px">WELCOME TO OUR SITE</div>
<svg class="abs divider" style="top:1475px" viewBox="0 0 36 10"><line x1="0" y1="5" x2="36" y2="5" stroke="#c8102e" stroke-width="2"/><ellipse cx="18" cy="5" rx="7" ry="4.5" fill="#ececee" stroke="#c8102e" stroke-width="2"/></svg>
<p class="abs welcome-text">There are many variations of passages of Lorem Ipsum available, but the majority have suffered alteration in some form, by injected humour, or randomised words which don't look even slightly believable. If you are going to use a passage of Lorem Ipsum, you need to be sure there isn't anything embarrassing hidden in the middle of text.All the Lorem Ipsum generators on the Internet tend to repeat predefined chunks as necessary.</p>
<div class="abs cert" style="left:441px;top:1673px;width:134px" role="img" aria-label="Bulwark+ certification badge"></div>
<div class="abs cert" style="left:647px;top:1673px;width:92px" role="img" aria-label="Veltrona K7 certification badge"></div>
<div class="abs btn read-more-center">READ MORE</div>

<!-- blog -->
<div class="abs section-title" style="top:1888px">LATEST BLOG</div>
<svg class="abs divider" style="top:1929px" viewBox="0 0 36 10"><line x1="0" y1="5" x2="36" y2="5" stroke="#c8102e" stroke-width="2"/><ellipse cx="18" cy="5" rx="7" ry="4.5" fill="#fff" stroke="#c8102e" stroke-width="2"/></svg>

<article class="abs card" style="left:133px">
  <div class="card-photo" role="img" aria-label="Hands repairing a laptop motherboard with a screwdriver" style="background:linear-gradient(135deg,#d9b89a,#7a6a5c 60%,#3b4a3a)"></div>
  <h3 class="card-title">It is a long established fact that a will be distracted by the</h3>
  <p class="card-text">The standard chunk of Lorem Ipsum used since the 1500s is reproduced below for those</p>
  <span class="btn card-btn">READ MORE</span>
</article>
<article class="abs card" style="left:451px">
  <div class="card-photo" role="img" aria-label="Close-up of a technician working on a computer circuit board" style="background:linear-gradient(135deg,#6f8fa8,#3a4e60 55%,#b0a070)"></div>
  <h3 class="card-title">Contrary to popular belief, Lorem Ipsum is not simply random</h3>
  <p class="card-text">The standard chunk of Lorem Ipsum used since the 1500s is reproduced below for those</p>
  <span class="btn card-btn">READ MORE</span>
</article>
<article class="abs card" style="left:770px">
  <div class="card-photo" role="img" aria-label="Glowing blue abstract circuit board pattern" style="background:radial-gradient(circle at 50% 50%,#7fd0ff,#1d6aa8 45%,#0a1f3d)"></div>
  <h3 class="card-title">There are many variations of passages of Lorem Ipsum available</h3>
  <p class="card-text">The standard chunk of Lorem Ipsum used since the 1500s is reproduced below for those</p>
  <span class="btn card-btn">READ MORE</span>
</article>

<!-- footer -->
<footer class="abs footer"></footer>
<div class="abs footer-brand"><span class="brand-mark"></span><span class="brand-name">LOpalo</span></div>
<div class="abs copyright">Copyrights @ 2017 All Rights Reserved</div>

<div class="abs foot-head" style="left:432px">CONTACT US</div>
<div class="abs foot-item" style="left:436px;top:2496px">
  <svg width="9" height="12" viewBox="0 0 10 14"><path d="M5 0a5 5 0 0 1 5 5c0 4-5 9-5 9S0 9 0 5a5 5 0 0 1 5-5z" fill="#fff"/><circle cx="5" cy="5" r="2" fill="#444"/></svg>
  <span>1450 Mesa Verde Lane<br>Santa Fe, NM 87501</span>
</div>
<div class="abs foot-item" style="left:436px;top:2555px">
  <svg width="10" height="10" viewBox="0 0 24 24"><path fill="#fff" d="M6.6 10.8c1.4 2.8 3.8 5.1 6.6 6.6l2.2-2.2c.3-.3.7-.4 1-.2 1.1.4 2.3.6 3.6.6.6 0 1 .4 1 1V20c0 .6-.4 1-1 1C10.6 21 3 13.4 3 4c0-.6.4-1 1-1h3.5c.6 0 1 .4 1 1 0 1.3.2 2.5.6 3.6.1.3 0 .7-.2 1L6.6 10.8z"/></svg>
  <span>888.888.8888</span>
</div>
<div class="abs foot-item" style="left:436px;top:2599px">
  <svg width="11" height="9" viewBox="0 0 12 9"><rect width="12" height="9" fill="#fff"/><path d="M0 0l6 5 6-5" fill="none" stroke="#444"/></svg>
  <span>info@lopalo.com</span>
</div>

<div class="abs foot-head" style="left:688px">MENU</div>
<ul class="abs menu-list"><li>HOME</li><li>ABOUT US</li><li>SERVICES</li><li>BLOG</li><li>TESTIMONIALS</li><li>CONTACT US</li></ul>

<div class="abs foot-head" style="left:888px">FOLLOW US</div>
<div class="abs social"><span aria-label="Social link"></span><span aria-label="Social link"></span><span aria-label="Social link" style="background:#3c7ab0"></span></div>

</body>
</html>
```